Designer Instructions – Updated Referral Program Flyer

(Based on the mock-up in “Brief Layout and Instructions.pdf”)

OVERALL STYLE + LAYOUT

Maintain the same general layout, structure, and flow as the mock-up flyer (front and back).

This is an update of an older flyer, not a full redesign — keep the same sections, proportions, and overall visual feel, but with cleaner, more modern design improvements.

The final flyer should look clean, bold, professional, and high-impact, geared toward realtors, property managers, and contractors who refer work.

FRONT SIDE INSTRUCTIONS
1. Header Section

Remove the Tallow Ridge Builders logo from the top banner.
(Shown on page 1 of the PDF)

2. Main Headline

Keep the same three-line structure:
EARN
UNLIMITED
CASH

Center it, maximize impact, and increase the font size of CASH so all three words match in importance.

Make the headline bold, clean, and the main focal point.

3. Cash Incentive Box

Keep the "$500 minimum OR 10% per referral" box, but upgrade the graphics to look sharper and more modern.

Ensure the wording matches exactly what’s in the mock-up.

4. Premier Partner Program Ribbon

Clean up and modernize the "PREMIER PARTNER PROGRAM" bar while keeping the same position and structure.

Ensure the checkmark badge remains crisp and professional.

5. Supporting Icons Section

Keep the four icons/benefit boxes (Guaranteed Payout, Free Evaluations, Affordable Solutions, Industry Leaders) in the same order.

Update the icons to cleaner, more modern styles — but maintain the same meanings.

Improve alignment and spacing for sharper visual consistency.

6. Remove Icons in Contact Area

At the bottom (“CALL TEXT OR BOOK ONLINE 555-014-2796 TallowRidgeBuilders.example”), remove the phone and internet icons, as noted on page 2 of the PDF.

7. Replace All Images

I (Darnell) will provide all updated stock images separately via email.

Replace the flood/water-damage imagery and roof leak with the new images I send.

Keep image placement and proportions the same as the mock-up.

BACK SIDE INSTRUCTIONS
1. Header Image + “REFER / EARN” Section

Maintain the same large split-image layout (“The more you refer, the more you earn”).

Replace all background imagery with the new assets I will send.

Keep the CASH FLOW image section but modernize the type and spacing.

2. “HOW IT WORKS” Section

Preserve the three-column layout:

Refer Flood, Water & Mold Damage

We Take Care of Everything (evaluations/insurance)

Get Paid to Share

Update images, tighten spacing, and use modern iconography.

3. Remove Phone/Internet Icons

Same as the front side — remove small communication icons and keep only the text/number/URL.

4. Bottom Contact Bar

Keep the blue bar, same wording, same layout — just modernize the style if needed for clarity.

5. Replace All Back-Side Images

Again, I will email you the image assets.

Keep the layout EXACT — just update with higher-quality photos and improved design.

TEXT CONTENT (Keep as-is unless spacing adjustments needed)

All text shown in the PDF should remain exactly the same unless spacing or visual balance requires minor adjustments.
Example from page 3:

“REFER FLOOD, MOLD & CONSTRUCTION JOBS”

“We Schedule a Free Estimate. If Approved, You Get Paid.”

“Everybody Benefits From Referrals”

Everything stays, just refreshed and visually improved.

DESIGN GOALS

Flyer should look high-end and trustworthy, not salesy.

Consistent color theme: blues, whites, yellows, same palette as original.

Use bold, modern fonts with strong readability.

Ensure all headlines pop and all benefit boxes are clean, well-aligned, and evenly spaced.

The final result should feel like a premium referral program flyer for a top-tier restoration/remodel company.

FILES I WILL PROVIDE

I will send the designer:

All replacement stock photos

Any updated logos (if needed)

Original high-resolution version of the mock-up (if available)

Any additional icons preferred

0054AA
0677BA
7BADD7
CADEEF
E8F1F8

• Designer Instructions – Updated Referral Program Flyer (Based on the mock-up in “Brief Layout and Instructions.pdf”) OVERALL STYLE + LAYOUT Maintain the same general layout, structure, and flow as the mock-up flyer (front and back). This is an update of an older flyer, not a full redesign — keep the same sections, proportions, and overall visual feel, but with cleaner, more modern design improvements. The final flyer should look clean, bold, professional, and high-impact, geared toward realtors, property managers, and contractors who refer work. FRONT SIDE INSTRUCTIONS 1. Header Section Remove the Tallow Ridge Builders logo from the top banner. (Shown on page 1 of the PDF) 2. Main Headline Keep the same three-line structure: EARN UNLIMITED CASH Center it, maximize impact, and increase the font size of CASH so all three words match in importance. Make the headline bold, clean, and the main focal point. 3. Cash Incentive Box Keep the "$500 minimum OR 10% per referral" box, but upgrade the graphics to look sharper and more modern. Ensure the wording matches exactly what’s in the mock-up. 4. Premier Partner Program Ribbon Clean up and modernize the "PREMIER PARTNER PROGRAM" bar while keeping the same position and structure. Ensure the checkmark badge remains crisp and professional. 5. Supporting Icons Section Keep the four icons/benefit boxes (Guaranteed Payout, Free Evaluations, Affordable Solutions, Industry Leaders) in the same order. Update the icons to cleaner, more modern styles — but maintain the same meanings. Improve alignment and spacing for sharper visual consistency. 6. Remove Icons in Contact Area At the bottom (“CALL TEXT OR BOOK ONLINE 555-014-2796 TallowRidgeBuilders.example”), remove the phone and internet icons, as noted on page 2 of the PDF. 7. Replace All Images I (Darnell) will provide all updated stock images separately via email. Replace the flood/water-damage imagery and roof leak with the new images I send. Keep image placement and proportions the same as the mock-up. BACK SIDE INSTRUCTIONS 1. Header Image + “REFER / EARN” Section Maintain the same large split-image layout (“The more you refer, the more you earn”). Replace all background imagery with the new assets I will send. Keep the CASH FLOW image section but modernize the type and spacing. 2. “HOW IT WORKS” Section Preserve the three-column layout: Refer Flood, Water & Mold Damage We Take Care of Everything (evaluations/insurance) Get Paid to Share Update images, tighten spacing, and use modern iconography. 3. Remove Phone/Internet Icons Same as the front side — remove small communication icons and keep only the text/number/URL. 4. Bottom Contact Bar Keep the blue bar, same wording, same layout — just modernize the style if needed for clarity. 5. Replace All Back-Side Images Again, I will email you the image assets. Keep the layout EXACT — just update with higher-quality photos and improved design. TEXT CONTENT (Keep as-is unless spacing adjustments needed) All text shown in the PDF should remain exactly the same unless spacing or visual balance requires minor adjustments. Example from page 3: “REFER FLOOD, MOLD & CONSTRUCTION JOBS” “We Schedule a Free Estimate. If Approved, You Get Paid.” “Everybody Benefits From Referrals” Everything stays, just refreshed and visually improved. DESIGN GOALS Flyer should look high-end and trustworthy, not salesy. Consistent color theme: blues, whites, yellows, same palette as original. Use bold, modern fonts with strong readability. Ensure all headlines pop and all benefit boxes are clean, well-aligned, and evenly spaced. The final result should feel like a premium referral program flyer for a top-tier restoration/remodel company. FILES I WILL PROVIDE I will send the designer: All replacement stock photos Any updated logos (if needed) Original high-resolution version of the mock-up (if available) Any additional icons preferred

```html
<!DOCTYPE html>
<html lang="en">
<head>
<meta charset="utf-8">
<title>Referral Program Flyer – Tallow Ridge Builders</title>
<link rel="stylesheet" href="https://fonts.googleapis.com/css2?family=Montserrat:wght@600;700;800;900&display=swap">
<style>
:root{
  --blue:#0a57b8;
  --blue-deep:#0b3f95;
  --blue-bright:#1a78d6;
  --navy:#1c2f72;
  --yellow:#ffe11a;
  --gold:#ffc21a;
  --orange:#f08a1c;
  --orange-deep:#c9590e;
  --red:#e4232b;
  --white:#ffffff;
  --page:#efefef;
  --ink:#1c2f72;
}
*{box-sizing:border-box;margin:0;padding:0}
html,body{width:915px;height:1200px;overflow:hidden;background:var(--page)}
body{font-family:"Montserrat",Arial,sans-serif;position:relative}
.card{position:absolute;left:48px;width:818px;height:530px;background:var(--white);overflow:hidden;box-shadow:0 4px 12px rgba(0,0,0,.18)}
.card--front{top:48px}
.card--back{top:615px}

/* hero panels */
.hero{position:absolute;left:0;top:0;width:818px;background:radial-gradient(circle at 30% 40%,var(--blue-bright) 0%,var(--blue) 45%,var(--blue-deep) 100%)}
.hero--front{height:301px}
.hero--back{height:279px}
.photo{position:absolute;top:0;right:0}
.photo--house{width:430px;height:301px;background:linear-gradient(160deg,#e8e6e0 0%,#b9b4a8 40%,#7a8a5c 75%,#4f6640 100%);clip-path:polygon(72px 0,100% 0,100% 100%,72px 100%,0 147px)}
.photo-edge--front{position:absolute;top:0;left:378px;width:90px;height:301px;background:linear-gradient(90deg,#c9ced8,#f4f5f7);clip-path:polygon(82px 0,90px 0,18px 147px,90px 301px,82px 301px,10px 147px)}
.photo--cash{left:372px;height:279px;background:linear-gradient(150deg,#e4e6dc 0%,#c9cdbd 45%,#a8b0a0 100%);clip-path:polygon(80px 0,100% 0,100% 100%,0 100%)}
.photo-edge--back{position:absolute;top:0;left:362px;width:100px;height:279px;background:#e9ecf1;clip-path:polygon(90px 0,100px 0,10px 279px,0 279px)}
.tab-24{position:absolute;top:0;right:14px;width:76px;height:88px;background:var(--red);border-radius:0 0 8px 8px}
.tab-24::after{content:"";position:absolute;left:12px;top:10px;width:52px;height:52px;border-radius:50%;background:var(--white)}

/* headlines */
.headline{position:absolute;text-align:center;font-weight:900;line-height:.95;color:var(--white);letter-spacing:-1px}
.headline--front{left:20px;width:400px;top:18px}
.headline .l1{font-size:80px;display:block;text-shadow:0 3px 0 var(--orange),0 6px 0 var(--orange-deep),0 8px 10px rgba(0,0,0,.3)}
.headline .l2{font-size:41px;display:block;margin-top:6px;text-shadow:0 3px 0 var(--orange),0 5px 0 var(--orange-deep),0 7px 8px rgba(0,0,0,.3)}
.headline .l3{font-size:90px;display:block;color:var(--gold);margin-top:4px;text-shadow:0 3px 0 var(--orange),0 6px 0 var(--orange-deep),0 9px 10px rgba(0,0,0,.35)}
.headline--back{left:40px;width:290px;top:14px;color:var(--gold);line-height:.9;letter-spacing:-1.5px}
.headline--back .small{display:block;font-size:31px;text-shadow:0 2px 0 var(--orange),0 4px 0 var(--orange-deep)}
.headline--back .big{display:block;font-size:66px;text-shadow:0 3px 0 var(--orange),0 6px 0 var(--orange-deep),0 8px 8px rgba(0,0,0,.3)}

.ribbon{position:absolute;background:var(--yellow);color:var(--navy);font-weight:900;display:flex;align-items:center;justify-content:center;border-radius:16px 0 0 0;clip-path:polygon(0 0,100% 0,96% 100%,0 100%)}
.ribbon--front{left:30px;top:242px;width:440px;height:42px;font-size:26px;letter-spacing:.3px}
.ribbon--back{left:45px;top:213px;width:350px;height:51px;font-size:38px}

/* incentive pill */
.incentive{position:absolute;left:87px;top:301px;width:318px;height:46px;display:flex;border-radius:0 0 0 14px;overflow:hidden}
.incentive__min{width:108px;background:var(--navy);color:var(--yellow);font-weight:900;padding:6px 0 0 22px;line-height:.85}
.incentive__min b{font-size:22px}
.incentive__min b sup{font-size:11px}
.incentive__min span{display:block;font-size:10px}
.incentive__pct{flex:1;background:var(--yellow);color:var(--navy);font-weight:900;display:flex;align-items:center;padding-left:34px;gap:4px;border-radius:0 0 14px 0}
.incentive__pct b{font-size:33px;letter-spacing:-1px}
.incentive__pct span{font-size:13px;line-height:.95}
.incentive__or{position:absolute;left:90px;top:3px;width:40px;height:40px;border-radius:50%;background:var(--white);color:var(--navy);font-weight:900;font-size:13px;display:flex;align-items:center;justify-content:center}

/* premier program */
.premier-tab{position:absolute;left:498px;top:273px;width:136px;height:24px;background:linear-gradient(#fff,#dfe2e8);border-radius:10px 10px 0 0;font-weight:800;font-size:13px;letter-spacing:6px;color:var(--navy);text-align:center;line-height:24px}
.program{position:absolute;left:413px;top:301px;width:318px;height:46px;display:flex;font-weight:900;font-size:20px;color:var(--white)}
.program__left{flex:1;background:var(--red);border-radius:10px 0 0 10px;display:flex;align-items:center;padding-left:9px}
.program__right{flex:1;background:var(--navy);border-radius:0 10px 10px 0;display:flex;align-items:center;justify-content:flex-end;padding-right:12px}
.program__shield{position:absolute;left:130px;top:-6px;width:58px;height:62px}

.tagline{position:absolute;left:0;width:818px;text-align:center;font-weight:900;color:var(--navy);white-space:nowrap}
.tagline em{font-style:normal;color:var(--red)}
.tagline--wins{top:350px;font-size:28.5px;letter-spacing:-.6px}
.tagline--grow{top:463px;font-size:19.5px;letter-spacing:-.4px}
.tagline--refer{top:456px;font-size:25px;letter-spacing:-.5px;color:var(--blue)}

/* benefits */
.benefit{position:absolute;top:385px;width:170px;height:73px}
.benefit__head{position:absolute;left:0;top:0;width:147px;height:36px;background:var(--navy);border-radius:10px 12px 0 0;color:var(--gold);font-weight:900;font-size:10.5px;line-height:1.1;padding:7px 0 0 12px}
.benefit__body{position:absolute;left:0;top:36px;width:160px;height:37px;background:linear-gradient(90deg,#f3f4f6,#c9ccd3);border-radius:0 0 0 10px;font-size:7.2px;font-weight:700;color:#222;line-height:1.2;padding:4px 38px 0 12px}
.benefit__icon{position:absolute;left:128px;top:20px;width:44px;height:44px;border-radius:50%;background:var(--red);border:3px solid var(--white);box-shadow:0 2px 4px rgba(0,0,0,.25)}
.benefit__icon svg{width:100%;height:100%}

/* contact bar */
.contact{position:absolute;left:0;top:491px;width:818px;height:39px}
.contact__label{position:absolute;left:0;top:0;width:348px;height:39px;background:var(--navy);clip-path:polygon(0 0,92% 0,100% 100%,0 100%);color:var(--white);font-weight:900;font-size:19.5px;line-height:39px;padding-left:13px;white-space:nowrap}
.contact__phone{position:absolute;left:358px;top:-8px;font-weight:900;font-size:36px;color:var(--navy);letter-spacing:-.5px;white-space:nowrap}
.contact__web{position:absolute;right:8px;top:13px;font-weight:600;font-size:9.6px;color:#222;white-space:nowrap}

/* how it works */
.step{position:absolute;top:294px;width:221px;height:156px;border-radius:12px;overflow:hidden;background:var(--navy)}
.step__photo{height:78px}
.step__photo--equip{background:linear-gradient(180deg,#d9d5cf 0%,#6cb0d8 70%,#3d89b8 100%)}
.step__photo--thermal{background:linear-gradient(90deg,#f1f1ee 0%,#d8d6d2 50%,#8b3bb0 75%,#f2a21d 100%)}
.step__photo--sign{background:linear-gradient(120deg,#9cc9ec 0%,#dfeefa 45%,#f7de1c 70%,#f7de1c 100%)}
.step__title{color:var(--gold);font-weight:900;font-size:13.4px;line-height:1.1;text-align:center;margin-top:6px;padding:0 6px}
.step__text{color:var(--white);font-weight:700;font-size:9px;line-height:1.35;text-align:center;margin-top:4px}
</style>
</head>
<body>

<section class="card card--front" aria-label="Referral flyer front">
  <div class="hero hero--front"></div>
  <div class="photo-edge--front"></div>
  <div class="photo photo--house" role="img" aria-label="Photo of a contractor holding a work estimate clipboard in front of a house"></div>
  <div class="tab-24" role="img" aria-label="Emergency service badge"></div>

  <h1 class="headline headline--front">
    <span class="l1">EARN</span>
    <span class="l2">UNLIMITED</span>
    <span class="l3">CASH</span>
  </h1>
  <div class="ribbon ribbon--front">GET PAID TOREFER A FLOOD</div>

  <div class="premier-tab">PREMIER</div>

  <div class="incentive">
    <div class="incentive__min"><b><sup>$</sup>500</b><span>MINIMUM</span></div>
    <div class="incentive__pct"><b>10%</b><span>PER<br>REFERRAL!</span></div>
    <div class="incentive__or">OR</div>
  </div>

  <div class="program">
    <div class="program__left">PARTNER</div>
    <div class="program__right">PROGRAM</div>
    <svg class="program__shield" viewBox="0 0 58 62" aria-hidden="true">
      <path d="M29 2 L54 10 V30 C54 46 42 56 29 60 C16 56 4 46 4 30 V10 Z" fill="#e6e8ec" stroke="#b8bcc6" stroke-width="2"/>
      <path d="M29 9 L47 15 V30 C47 42 38 50 29 53 C20 50 11 42 11 30 V15 Z" fill="#fff"/>
      <path d="M18 30 L26 38 L42 20" fill="none" stroke="#e4232b" stroke-width="7" stroke-linecap="round" stroke-linejoin="round"/>
    </svg>
  </div>

  <p class="tagline tagline--wins">PARTNER WITH US &amp; <em>EVERYBODY WINS!</em></p>

  <div class="benefit" style="left:36px">
    <div class="benefit__body">MINIMUM $500 OR 10% OF TOTAL INVOICE PAID FAST</div>
    <div class="benefit__head">GUARANTEED<br>PAYOUT</div>
    <div class="benefit__icon"><svg viewBox="0 0 44 44" aria-hidden="true"><circle cx="22" cy="18" r="8" fill="none" stroke="#fff" stroke-width="2.5"/><path d="M17 25 L14 34 L18 32 L20 36 L22 27 M27 25 L30 34 L26 32 L24 36 L22 27" fill="#fff"/></svg></div>
  </div>
  <div class="benefit" style="left:227px">
    <div class="benefit__body">FAST &amp; FREE INSPEC-TIONS &amp; WRITTEN ESTIMAT</div>
    <div class="benefit__head">FREE<br>ESTIMATES</div>
    <div class="benefit__icon"><svg viewBox="0 0 44 44" aria-hidden="true"><path d="M14 10 H26 L31 15 V34 H14 Z" fill="#fff"/><path d="M18 20 H27 M18 24 H27 M18 28 H24" stroke="#e4232b" stroke-width="2"/></svg></div>
  </div>
  <div class="benefit" style="left:418px">
    <div class="benefit__body">LOWEST OUT OF POCKET COSTS FOR YOUR CUSTOMERS</div>
    <div class="benefit__head">AFFORDABLE<br>SOLUTIONS</div>
    <div class="benefit__icon"><svg viewBox="0 0 44 44" aria-hidden="true"><path d="M22 10 C16 10 13 14 13 19 C13 23 16 25 17 28 H27 C28 25 31 23 31 19 C31 14 28 10 22 10 Z" fill="#fff"/><rect x="18" y="30" width="8" height="4" rx="1" fill="#fff"/></svg></div>
  </div>
  <div class="benefit" style="left:609px">
    <div class="benefit__body">LICENSED &amp; CERTIFIED EXPERTS PROVIDE 100% GUARANTEE</div>
    <div class="benefit__head">INDUSTRY<br>LEADERS</div>
    <div class="benefit__icon"><svg viewBox="0 0 44 44" aria-hidden="true"><circle cx="22" cy="22" r="11" fill="none" stroke="#fff" stroke-width="2.5"/><path d="M16 22 L20 26 L28 18" fill="none" stroke="#fff" stroke-width="3" stroke-linecap="round" stroke-linejoin="round"/></svg></div>
  </div>

  <p class="tagline tagline--grow">SEND REFERRALS. GET PAID. <em>GROW YOUR BUSINESS.</em></p>

  <div class="contact">
    <div class="contact__label">CALL, TEXT OR BOOK ONLINE</div>
    <div class="contact__phone">555-014-2796</div>
    <div class="contact__web">www.TallowRidgeBuilders.example</div>
  </div>
</section>

<section class="card card--back" aria-label="Referral flyer back">
  <div class="hero hero--back"></div>
  <div class="photo-edge--back"></div>
  <div class="photo photo--cash" role="img" aria-label="Photo of hundred dollar bills with letter tiles spelling CASH FLOW"></div>

  <h2 class="headline headline--back">
    <span class="small">THE MORE YOU</span>
    <span class="big">REFER</span>
    <span class="small">THE MORE YOU</span>
    <span class="big">EARN</span>
  </h2>
  <div class="ribbon ribbon--back">HOW IT WORKS</div>

  <div class="step" style="left:53px">
    <div class="step__photo step__photo--equip" role="img" aria-label="Photo of water damage drying fans and dehumidifiers in a room"></div>
    <p class="step__title">REFER FLOOD, MOLD &amp; CONSTRUCTION JOBS:</p>
    <p class="step__text">IT'S SIMPLE TO REFER 24/7:<br>CALL, TEXT OR BOOK ONLINE.</p>
  </div>
  <div class="step" style="left:300px">
    <div class="step__photo step__photo--thermal" role="img" aria-label="Photo of a thermal imaging camera inspecting a wall"></div>
    <p class="step__title">WE TAKE CARE OF EVERYTHING:</p>
    <p class="step__text">WE SCHEDULE A FREE ESTIMATE.<br>IF APPROVED, YOU GET PAID.</p>
  </div>
  <div class="step" style="left:545px">
    <div class="step__photo step__photo--sign" role="img" aria-label="Photo of a yellow road sign reading get paid to share against a blue sky"></div>
    <p class="step__title">EVERYBODY BENEFITS FROM REFERRALS</p>
    <p class="step__text">WE PROVIDE EXPERT QUALITY<br>WORK FOR AFORDABLE PRICE.</p>
  </div>

  <p class="tagline tagline--refer"><em>REFER:</em> FLOODS, REMODELS, RENOVATIONS &amp; REPAIRS</p>

  <div class="contact">
    <div class="contact__label">CALL, TEXT OR BOOK ONLINE</div>
    <div class="contact__phone">555-014-2796</div>
    <div class="contact__web">www.TallowRidgeBuilders.example</div>
  </div>
</section>

</body>
</html>
```